VELUNO Adaptations
Business Cards, Leaflet and Booth Design
Project: VELUNO Adaptations
VELUNO Adaptations  - Real Estate
Creative Brief
I want to create adaptations for my logo. They have to reflect the style of the logo and have to be very creative in both execution and concept.
Real Estate
Freelancers and start ups. Young, ambition and creative
I need to create Business Cards, Letterheads, Booth design and Folded 4 flyers for an exhibit that I have. All information and content for BC and flyers are in the attached files Designers can use any photos from http://www.pixmarrow.example as i have credit there and can buy the final images for them. but I prefer not to pass 3 images.
tkerrow tkerrow
are you okay with this instead of the businessmen image, its a nice illustration so you can play with the colors? http://www.pixmarrow.example/stock-illustration-5271934-the-crew.php?st=394ac27 What do you think?
Great On #22 I want to see the two images switched, the up goes down and the down goes up...
we are almost there :)
I like the left side with the logo, I really do not like the right side. the slogan should be in the middle and you should utilize the remaining images. Also the font is out of character
Pixwright Pixwright
Do you want full size single image on both side of booth?
#18 come on man you can do better than this, it is still the circular template. Try to follow the flyer.
So far so great but still I have some modifications if I may. #17 1. I don't need the mobile No. on the cover and the email is still Orwin in there. 2. I want the messy office image on the "what we are doing here" 3. I want the office image next to "Rental Packs " 4. The meeting room images next to "how do we stand out" If you do this we are done, send my the links for the additional images so I can buy them...
one more thing, on #16 can you go through the text, its jumping lines. e.g. propose a solution is coming on 2 lines instead of 1. NICE JOB man
#16 Please change the image next to "what are doing here?" to the one next to the rental packs and vice-versa. Make the launch dat font smaller at least by 50% Finally use the email info@veluno.example instead Orwin. For the Booth #13,14,15, the template is circular which do not match the logo. Do not use the People images. Just play on the 3 I provided. Use the logo on one side and slogan on the other. No need for more text.
These are just examples to give you an idea The space http://www.pixmarrow.example/stock-photo-26481937-office-building-with-several-workstations.php?st=5392c84 The hassle of working from home http://www.pixmarrow.example/stock-photo-27395146-very-messy-desk.php?st=5392c84 meeting rooms http://www.pixmarrow.example/stock-photo-26917483-contemporary-office-board-room.php?st=9e415d2
Can you do me a favor, I search lots of images but actually I do not understand your business related images. Can you please reach some links for me! So that I got which type of images you want.
# 11 I like the template, but can you choose images that do not have people. I am from Saudi Arabia and Western looking people would not work. You can put meeting rooms or more diversified people images.
On #9 BC blue back, can I see a white logo option.
oh on the preview the colors are missed up but when i open the page its okay. Anyways here's my final comments, overall i prefer the blue back with a white logo. On #4 can I see the blue box name with sharp edges On #1 make my name a bit bigger.
Sorry but where is the yellow in #4?
fine crafter, forget the yellow for the #4, can I see it in blue and white.

```html
<!DOCTYPE html>
<html lang="en">
<head>
<meta charset="utf-8">
<title>VELUNO Adaptations – Stationery, Flyer and Booth</title>
<link rel="stylesheet" href="https://fonts.googleapis.com/css2?family=Montserrat:wght@300;400;600&display=swap">
<style>
  :root{
    --bg:#e6e8eb;
    --blue:#1f5fa8;
    --blue-dark:#143f75;
    --blue-light:#d4e5f4;
    --white:#ffffff;
    --ink:#2c3440;
    --grey:#8a94a0;
    --photo-room:#b9c7d3;
    --photo-desk:#cfd6dc;
  }
  *{box-sizing:border-box;margin:0;padding:0}
  html,body{width:1200px;height:674px;overflow:hidden}
  body{background:var(--bg);font-family:"Montserrat",sans-serif;color:var(--ink);position:relative}
  .piece{position:absolute;background:var(--white);box-shadow:0 2px 6px rgba(0,0,0,.18);overflow:hidden}
  .photo{position:absolute}
  .brand{font-family:"Montserrat",sans-serif;font-weight:600;color:var(--blue);letter-spacing:.12em;display:flex;align-items:center;gap:.35em}
  .brand-mark{display:inline-block;width:.8em;height:.8em;background:currentColor}
  .brand.on-blue{color:var(--white)}
  .tagline{font-size:7px;letter-spacing:.2em;color:var(--grey);margin-top:2px}

  /* booth */
  .booth-logo{left:77px;top:72px;width:283px;height:288px}
  .booth-slogan{left:370px;top:72px;width:314px;height:288px}
  .booth-band{position:absolute;left:0;right:0;top:0;height:10px;background:var(--blue)}
  .booth-logo .photo{left:0;right:0;top:10px;bottom:0;background:linear-gradient(180deg,#e9eff4 0%,var(--photo-room) 60%,#8c9aa6 100%)}
  .booth-logo .brand-block{position:absolute;left:24px;top:46px}
  .booth-logo .brand{font-size:26px}
  .booth-slogan .photo{left:0;right:0;top:10px;bottom:0;background:linear-gradient(180deg,#dfe6ec 0%,var(--photo-desk) 55%,#9aa4ad 100%)}
  .slogan{position:absolute;left:0;right:0;top:118px;text-align:center;font-weight:300;font-size:22px;letter-spacing:.08em;color:var(--ink)}

  /* flyer spread */
  .spread{left:701px;top:72px;width:259px;height:456px;background:transparent;box-shadow:none}
  .spread-top,.spread-bottom{position:absolute;left:0;width:259px;background:var(--white);box-shadow:0 2px 6px rgba(0,0,0,.18);overflow:hidden}
  .spread-top{top:0;height:204px}
  .spread-bottom{top:218px;height:238px}
  .col-left{position:absolute;left:0;top:0;width:96px;height:100%;border-right:1px solid #e3e8ee}
  .col-right{position:absolute;left:96px;top:0;right:0;height:100%;background:linear-gradient(180deg,#fff 0%,var(--blue-light) 100%)}
  .spread-top .col-left .photo{left:6px;top:8px;width:84px;height:58px;background:linear-gradient(135deg,#5b6a78,#9aa8b5)}
  .spread-top .col-right .photo{left:6px;top:8px;right:6px;height:72px;background:linear-gradient(135deg,#c7d2dc,#7f8d99)}
  .panel-head{position:absolute;left:6px;top:74px;width:84px;height:10px;background:var(--blue)}
  .panel-text{position:absolute;left:6px;top:90px;width:84px;font-size:6px;line-height:1.5;color:var(--ink)}
  .spread-top .brand-block{position:absolute;left:0;right:0;top:112px;display:flex;flex-direction:column;align-items:center}
  .spread-top .brand{font-size:16px}
  .section-head{position:absolute;left:6px;top:10px;width:84px;background:var(--blue);color:var(--white);font-size:6px;font-weight:600;padding:2px 4px}
  .spread-bottom .panel-text{top:28px}
  .rows{position:absolute;left:6px;top:120px;width:84px}
  .rows span{display:block;height:1px;background:#c9d3dd;margin-bottom:8px}
  .spread-bottom .col-right .photo{left:6px;top:10px;right:6px;height:118px;background:linear-gradient(160deg,#e8eef3,#a9b6c1)}
  .spread-bottom .brand-block{position:absolute;left:50px;top:150px}
  .spread-bottom .brand{font-size:14px}

  /* stacked flyers */
  .flyer{width:62px;height:210px}
  .flyer .head{position:absolute;left:0;right:0;top:0;height:12px;background:var(--blue)}
  .flyer .photo{left:4px;right:4px;top:18px;height:66px;background:linear-gradient(135deg,#c7d2dc,#7f8d99)}
  .flyer .brand-block{position:absolute;left:0;right:0;top:96px;display:flex;justify-content:center}
  .flyer .brand{font-size:9px}
  .flyer .foot{position:absolute;left:0;right:0;bottom:0;height:60px;background:linear-gradient(180deg,#fff,var(--blue-light))}
  .flyer-a{left:974px;top:96px;transform:rotate(-4deg)}
  .flyer-b{left:1012px;top:110px}
  .flyer-c{left:1050px;top:124px;transform:rotate(3deg)}
  .flyer-d{left:1020px;top:330px;transform:rotate(-2deg)}

  /* business cards */
  .card{width:84px;height:50px;padding:6px}
  .card .brand{font-size:9px}
  .card .name{font-size:5.5px;font-weight:600;margin-top:6px}
  .card .line{font-size:4.5px;color:var(--grey);line-height:1.4}
  .card-blue{background:var(--blue);display:flex;align-items:center;justify-content:center}
  .card-blue .wave{position:absolute;right:-20px;top:-10px;width:60px;height:70px;border-radius:50%;background:var(--blue-dark)}
  .card-blue .brand{position:relative}
  .card-back .bar{position:absolute;left:0;right:0;bottom:0;height:8px;background:var(--blue)}

  /* letterhead and envelope */
  .letterhead{left:283px;top:384px;width:120px;height:245px;padding:12px}
  .letterhead .brand{font-size:10px}
  .letterhead .fold{position:absolute;left:0;right:0;bottom:0;height:40px;background:linear-gradient(180deg,#fff,var(--blue-light))}
  .letterhead .contact{position:absolute;left:12px;bottom:8px;font-size:5px;color:var(--blue-dark)}
  .envelope{left:413px;top:444px;width:187px;height:120px}
  .envelope svg{position:absolute;left:0;top:0}
  .envelope .brand-block{position:absolute;left:12px;top:12px}
  .envelope .brand{font-size:10px}
  .envelope .contact{position:absolute;right:12px;bottom:10px;font-size:5px;color:var(--blue-dark)}
</style>
</head>
<body>

<!-- Booth -->
<section class="piece booth-logo">
  <div class="booth-band"></div>
  <div class="photo" role="img" aria-label="Photo of a contemporary boardroom with a long table and chairs"></div>
  <div class="brand-block">
    <div class="brand"><span class="brand-mark"></span>VELUNO</div>
    <div class="tagline">OFFICE MADE EASY</div>
  </div>
</section>

<section class="piece booth-slogan">
  <div class="booth-band"></div>
  <div class="photo" role="img" aria-label="Photo of an open office with workstations above a messy desk"></div>
  <p class="slogan">OFFICE MADE EASY</p>
</section>

<!-- Folded flyer spread -->
<section class="piece spread">
  <div class="spread-top">
    <div class="col-left">
      <div class="photo" role="img" aria-label="Photo of a cluttered home workspace"></div>
      <div class="panel-head"></div>
      <p class="panel-text">We build shared offices for freelancers and young teams.</p>
    </div>
    <div class="col-right">
      <div class="photo" role="img" aria-label="Illustration of a business team standing together"></div>
      <div class="brand-block">
        <div class="brand"><span class="brand-mark"></span>VELUNO</div>
        <div class="tagline">OFFICE MADE EASY</div>
      </div>
    </div>
  </div>
  <div class="spread-bottom">
    <div class="col-left">
      <div class="section-head">What we offer?</div>
      <p class="panel-text">Flexible desks, meeting rooms and rental packs for every stage.</p>
      <div class="rows"><span></span><span></span><span></span><span></span></div>
    </div>
    <div class="col-right">
      <div class="photo" role="img" aria-label="Photo of an office floor with several workstations"></div>
      <div class="brand-block">
        <div class="brand"><span class="brand-mark"></span>VELUNO</div>
      </div>
    </div>
  </div>
</section>

<!-- Stacked flyers -->
<section class="piece flyer flyer-a">
  <div class="head"></div>
  <div class="photo" role="img" aria-label="Illustration of a business team"></div>
  <div class="brand-block"><div class="brand">VELUNO</div></div>
  <div class="foot"></div>
</section>
<section class="piece flyer flyer-b">
  <div class="head"></div>
  <div class="photo" role="img" aria-label="Illustration of a business team"></div>
  <div class="brand-block"><div class="brand">VELUNO</div></div>
  <div class="foot"></div>
</section>
<section class="piece flyer flyer-c">
  <div class="head"></div>
  <div class="photo" role="img" aria-label="Illustration of a business team"></div>
  <div class="brand-block"><div class="brand">VELUNO</div></div>
  <div class="foot"></div>
</section>
<section class="piece flyer flyer-d">
  <div class="head"></div>
  <div class="photo" role="img" aria-label="Illustration of a business team"></div>
  <div class="brand-block"><div class="brand">VELUNO</div></div>
  <div class="foot"></div>
</section>

<!-- Business cards -->
<section class="piece card" style="left:80px;top:384px">
  <div class="brand"><span class="brand-mark"></span>VELUNO</div>
  <p class="name">Tomas Heller</p>
  <p class="line">Founder</p>
  <p class="line">info@veluno.example</p>
</section>
<section class="piece card" style="left:80px;top:442px">
  <div class="brand"><span class="brand-mark"></span>VELUNO</div>
  <p class="name">Tomas Heller</p>
  <p class="line">Founder</p>
  <p class="line">info@veluno.example</p>
</section>
<section class="piece card" style="left:80px;top:500px">
  <div class="brand"><span class="brand-mark"></span>VELUNO</div>
  <p class="name">Tomas Heller</p>
  <p class="line">Founder</p>
  <p class="line">info@veluno.example</p>
</section>
<section class="piece card card-back" style="left:174px;top:384px">
  <div class="brand"><span class="brand-mark"></span>VELUNO</div>
  <p class="line" style="margin-top:6px">Flexible offices for young teams</p>
  <div class="bar"></div>
</section>
<section class="piece card card-back" style="left:174px;top:442px">
  <div class="brand"><span class="brand-mark"></span>VELUNO</div>
  <p class="line" style="margin-top:6px">Flexible offices for young teams</p>
  <div class="bar"></div>
</section>
<section class="piece card card-blue" style="left:174px;top:500px">
  <div class="wave"></div>
  <div class="brand on-blue"><span class="brand-mark"></span>VELUNO</div>
</section>

<!-- Letterhead -->
<section class="piece letterhead">
  <div class="brand"><span class="brand-mark"></span>VELUNO</div>
  <div class="fold"></div>
  <p class="contact">info@veluno.example</p>
</section>

<!-- Envelope -->
<section class="piece envelope">
  <svg width="187" height="120" viewBox="0 0 187 120" aria-hidden="true">
    <path d="M0 0 H187 V18 L93.5 60 L0 18 Z" fill="var(--blue)"/>
    <path d="M0 18 L93.5 60 L187 18" fill="none" stroke="var(--blue-dark)" stroke-width="1"/>
    <rect x="0" y="108" width="187" height="12" fill="var(--blue-light)"/>
  </svg>
  <div class="brand-block" style="top:70px"><div class="brand"><span class="brand-mark"></span>VELUNO</div></div>
  <p class="contact">info@veluno.example</p>
</section>

</body>
</html>
```